High End International Drug and Alcohol Recovery Service Needs a Brochure Design

We need a flyer design for a high end, private, drug, alcohol and addiction recovery firm. We are based in Los Angeles. We want the flyer to be a bi-fold or trifold. We want it to have a sleek, modern look but conveys the message that we are here to support our clients and help them through difficult times. We want to be approachable.
I am attaching picstures for you all to use.

Target Market(s)

High end clients, affluent clientele.

Industry/Entity Type

Life Coaching

Requirements
Must have
• Must have our logo on the back.
Nice to have
• Our slogans somewhere in there, "find your path" and "build your future."

```html
<!DOCTYPE html>
<html lang="en">
<head>
<meta charset="utf-8">
<title>Clearpath Living – Trifold Brochure</title>
<link href="https://fonts.googleapis.com/css2?family=Montserrat:wght@600;700;800&family=Open+Sans:ital,wght@0,400;0,600;0,700;1,400&display=swap" rel="stylesheet">
<style>
  :root{
    --orange:#f7941d;
    --orange-deep:#e27b0c;
    --navy:#1d2942;
    --navy-2:#2a3858;
    --ink:#4a4a4a;
    --muted:#7b7b7b;
    --backdrop:#3a3b3e;
    --paper:#ffffff;
  }
  *{box-sizing:border-box;margin:0;padding:0}
  html,body{width:793px;height:1200px;overflow:hidden}
  body{background:var(--backdrop);font-family:"Open Sans",Arial,sans-serif;color:var(--ink);position:relative}
  .sheet{position:absolute;left:25px;width:743px;height:560px;display:grid;grid-template-columns:repeat(3,1fr);background:var(--paper);box-shadow:0 6px 18px rgba(0,0,0,.45);overflow:hidden}
  .sheet--outer{top:20px}
  .sheet--inner{top:615px}
  .panel{position:relative;overflow:hidden;height:560px}
  .panel + .panel{border-left:1px solid #e6e6e6}
  h2,h3,.heading{font-family:"Montserrat",Arial,sans-serif}
  .url{position:absolute;left:0;right:0;bottom:12px;text-align:center;font-size:9px;font-weight:700;color:var(--orange);letter-spacing:.3px}
  .url--light{color:#fff}

  /* services panel */
  .services{padding:16px 18px 0}
  .services__corner{position:absolute;top:0;right:0;width:70px;height:46px;background:var(--orange);clip-path:polygon(40% 0,100% 0,100% 100%)}
  .services h2{color:var(--orange);font-size:20px;font-weight:800;text-align:center;margin-bottom:10px}
  .services p{font-size:7.4px;line-height:1.55;text-align:justify;margin-bottom:12px}
  .services h3{color:var(--orange);font-size:11px;font-weight:800;margin-bottom:6px}
  .services ul{list-style:none;font-size:8px;font-weight:600;color:var(--orange);line-height:1.6}
  .services li::before{content:"• ";color:var(--orange)}
  .services__photo{position:absolute;left:0;right:0;bottom:0;height:215px;background:linear-gradient(160deg,#ffcf7a 0%,#f39a2c 45%,#b8560d 100%);clip-path:polygon(0 18%,100% 0,100% 100%,0 100%)}
  .services__band{position:absolute;left:0;right:0;bottom:197px;height:22px;background:var(--navy);clip-path:polygon(0 100%,100% 0,100% 35%,0 135%)}

  /* typical services panel */
  .typical{padding:16px 16px 0}
  .typical h3{color:var(--orange);font-size:9.5px;font-weight:800;line-height:1.3;margin-bottom:9px}
  .typical ul{list-style:none;font-size:7.3px;line-height:1.3}
  .typical li{padding:2.6px 0 2.6px 9px;border-bottom:1px solid #ececec;position:relative}
  .typical li::before{content:"";position:absolute;left:0;top:6px;width:4px;height:4px;background:var(--orange);border-radius:50%}
  .typical__stripe{position:absolute;left:0;right:0;bottom:32px;height:6px;background:var(--orange);transform:skewY(-4deg)}

  /* challenges panel */
  .challenges{background:var(--navy);color:#fff}
  .challenges__sky{position:absolute;inset:0 0 auto 0;height:210px;background:linear-gradient(180deg,#6e8db3 0%,#a9bfd6 60%,#d9c7a8 100%)}
  .challenges__box{position:absolute;left:0;right:0;top:0;height:210px;background:rgba(29,41,66,.82);padding:16px 16px 0}
  .challenges__box h3{font-size:10px;font-weight:800;margin-bottom:8px}
  .challenges__box ul{list-style:none;font-size:7.6px;line-height:1.65}
  .challenges__box li::before{content:"• ";color:var(--orange)}
  .challenges__group{position:absolute;left:0;right:0;top:210px;height:125px;background:linear-gradient(135deg,#c9a27b 0%,#8a6d55 50%,#3f4a5e 100%)}
  .challenges__list{position:absolute;left:16px;right:16px;top:350px;text-align:right}
  .challenges__item{margin-bottom:9px}
  .challenges__item h4{font-family:"Montserrat",Arial,sans-serif;color:var(--orange);font-size:8.6px;font-weight:700}
  .challenges__item p{font-size:7.2px;line-height:1.4;color:#e8ebf2}

  /* about panel */
  .about__photo{position:absolute;left:0;right:0;top:0;height:195px;background:linear-gradient(150deg,#f1d3a6 0%,#d79f6a 45%,#8b6448 100%);clip-path:polygon(0 0,100% 0,100% 86%,0 100%)}
  .about__band{position:absolute;left:0;right:0;top:176px;height:26px;background:var(--orange);clip-path:polygon(0 70%,100% 0,100% 28%,0 100%)}
  .about__body{position:absolute;left:18px;right:18px;top:212px}
  .about__body h2{color:var(--orange);font-size:17px;font-weight:800;margin-bottom:8px}
  .about__body p{font-size:7.3px;line-height:1.55;text-align:justify;margin-bottom:8px}

  /* contact panel */
  .contact__quote{position:absolute;left:18px;right:18px;top:20px;font-size:9px;font-style:italic;color:var(--muted);line-height:1.55}
  .contact__quote svg{display:block;margin-bottom:4px}
  .contact__accent{position:absolute;left:0;right:0;top:150px;height:40px;background:var(--orange);clip-path:polygon(0 100%,100% 0,100% 30%,0 130%)}
  .contact__panel{position:absolute;left:0;right:0;top:162px;bottom:0;background:var(--navy);clip-path:polygon(0 18%,100% 0,100% 100%,0 100%);padding:78px 20px 0;text-align:center}
  .contact__title{color:var(--orange);font-size:25px;font-weight:800;line-height:1}
  .contact__sub{color:#fff;font-family:"Montserrat",Arial,sans-serif;font-size:10px;font-weight:700;letter-spacing:.4px;margin:5px 0 14px}
  .contact__phone{display:flex;align-items:center;justify-content:center;gap:7px;color:var(--orange);font-family:"Montserrat",Arial,sans-serif;font-weight:800;font-size:17px}
  .contact__label{color:var(--orange);font-weight:700;font-size:11px;margin-top:12px}
  .contact__email{color:#fff;font-size:10px;font-weight:600}
  .contact__icon{margin:26px auto 0;width:46px;height:46px}

  /* back cover */
  .cover__brand{position:absolute;top:26px;left:50%;transform:translateX(-50%);display:flex;align-items:center;gap:7px;white-space:nowrap}
  .cover__brand-mark{width:12px;height:12px;background:var(--orange)}
  .cover__brand-name{font-family:"Montserrat",Arial,sans-serif;font-weight:700;font-size:17px;color:var(--navy)}
  .cover__photo{position:absolute;left:0;right:0;top:120px;bottom:40px;background:linear-gradient(180deg,#c8d3de 0%,#8fa1b4 35%,#6b5b4c 70%,#4a3d33 100%)}
</style>
</head>
<body>

<section class="sheet sheet--outer">
  <article class="panel services">
    <div class="services__corner"></div>
    <h2>SERVICES</h2>
    <p>Our team of recovery professionals works alongside each client in a discreet, private setting to build lasting change. We offer guidance at every stage of recovery, from the first difficult conversation to a stable daily routine. Every plan is shaped around personal goals, family needs and the pace that feels right. We believe recovery is possible for everyone, and we stay close through each step so that no one has to walk the path alone. Our approach blends proven methods with warm, human support, giving clients the tools to find their path and build their future with confidence and care.</p>
    <h3>PREMIUM SERVICE</h3>
    <ul>
      <li>24/7 Companion</li>
      <li>Recovery planning consultation</li>
      <li>Sober transition</li>
      <li>Support</li>
    </ul>
    <div class="services__band"></div>
    <div class="services__photo" role="img" aria-label="Silhouette of a climber reaching a summit against an orange sunset"></div>
  </article>

  <article class="panel typical">
    <h3>EXAMPLES OF TYPICAL SERVICES<br>INCLUDE (BUT NOT LIMITED TO)</h3>
    <ul>
      <li>Individualised support for clients in the real world</li>
      <li>Reintegration to returning to home, school or work post-rehab</li>
      <li>Working closely with your doctors, therapists and family</li>
      <li>Transportation to and from rehab</li>
      <li>Companion day trips</li>
      <li>Family meetings and guidance</li>
      <li>Life coaching</li>
      <li>Confidence building</li>
      <li>Accountability and general guidance</li>
      <li>Advocacy in court</li>
      <li>Advocacy when dealing with treatment centres</li>
      <li>Assistance with new place of lifestyle</li>
      <li>Life skills building</li>
      <li>Guidance while monitoring a lifestyle change</li>
      <li>Guidance with social interactions and public relations</li>
      <li>Advice regarding sound nutrition, diet, fitness and physical and emotional wellbeing</li>
      <li>Guidance with financial planning</li>
      <li>Family management</li>
      <li>Referral to treatment centres and therapists</li>
      <li>Client home management and supervision</li>
      <li>Problem solving</li>
      <li>Help in recovery</li>
    </ul>
    <div class="typical__stripe"></div>
    <div class="url">www.clearpathliving.com</div>
  </article>

  <article class="panel challenges">
    <div class="challenges__sky" role="img" aria-label="Open sky over a mountain landscape"></div>
    <div class="challenges__box">
      <h3>CHALLENGES WE CAN HELP WITH</h3>
      <ul>
        <li>Alcohol and drug dependency, abuse and addiction</li>
        <li>Dual Diagnosis</li>
        <li>Traumatic brain injuries</li>
        <li>Depression</li>
        <li>Social anxiety</li>
        <li>And more</li>
      </ul>
    </div>
    <div class="challenges__group" role="img" aria-label="Group of friends sitting together outdoors"></div>
    <div class="challenges__list">
      <div class="challenges__item"><h4>Companionship</h4><p>Provide the ideal companion and support you or your loved one.</p></div>
      <div class="challenges__item"><h4>Recovery Planning</h4><p>Private planning that provides success.</p></div>
      <div class="challenges__item"><h4>Creating Balanced Lifestyle</h4><p>Helping clients learn to flourish.</p></div>
      <div class="challenges__item"><h4>Privacy &amp; Confidentiality</h4><p>We adhere to the strictest of confidentiality standards.</p></div>
    </div>
  </article>
</section>

<section class="sheet sheet--inner">
  <article class="panel about">
    <div class="about__photo" role="img" aria-label="Two women sharing a supportive embrace"></div>
    <div class="about__band"></div>
    <div class="about__body">
      <h2>ABOUT US</h2>
      <p>Clearpath Living is a recovery, support and lifestyle service dedicated to improving the quality of life and re-establishing the stability of clients.</p>
      <p>Our team of dedicated and caring mentors are on hand to work with your needs. Your recovery plan is designed to give you clarity, direction and the confidence to move forward each day.</p>
      <p>We work side by side with families, doctors and therapists so that every part of your life is supported. We listen first, then act with care and respect for your privacy at all times.</p>
      <p>We have the necessary experience to guide you from the early days of treatment to a steady, balanced life. Our mission is simple: help you find your path and build your future.</p>
    </div>
    <div class="url">www.clearpathliving.com</div>
  </article>

  <article class="panel contact">
    <div class="contact__quote">
      <svg width="16" height="12" viewBox="0 0 16 12" aria-hidden="true"><path fill="#f7941d" d="M0 12V7C0 3 2 0.8 6 0l.6 1.5C4.6 2.3 3.6 3.6 3.5 5.5H6.5V12zM9 12V7c0-4 2-6.2 6-7l.6 1.5c-2 .8-3 2.1-3.1 4H15.5V12z"/></svg>
      Recovery often prepares ordinary people for an extraordinary destiny, and we are here for every step.
    </div>
    <div class="contact__accent"></div>
    <div class="contact__panel">
      <div class="heading contact__title">GET IN TOUCH</div>
      <div class="contact__sub">SPEAK TO SOMEONE NOW</div>
      <div class="contact__phone">
        <svg width="16" height="16" viewBox="0 0 24 24" aria-hidden="true"><path fill="#f7941d" d="M6.6 10.8a15.1 15.1 0 0 0 6.6 6.6l2.2-2.2a1 1 0 0 1 1-.25 11.4 11.4 0 0 0 3.6.57 1 1 0 0 1 1 1V20a1 1 0 0 1-1 1A17 17 0 0 1 3 4a1 1 0 0 1 1-1h3.5a1 1 0 0 1 1 1c0 1.25.2 2.45.57 3.57a1 1 0 0 1-.25 1z"/></svg>
        (888) 555-0142
      </div>
      <div class="contact__label">Email</div>
      <div class="contact__email">info@clearpathliving.com</div>
      <svg class="contact__icon" viewBox="0 0 46 46" aria-hidden="true">
        <rect width="46" height="46" rx="6" fill="#f7c21d"/>
        <rect x="10" y="14" width="26" height="18" rx="2" fill="none" stroke="#1d2942" stroke-width="2.4"/>
        <path d="M10.5 15l12.5 10 12.5-10" fill="none" stroke="#1d2942" stroke-width="2.4"/>
      </svg>
      <div class="url url--light">www.clearpathliving.com</div>
    </div>
  </article>

  <article class="panel cover">
    <div class="cover__brand">
      <span class="cover__brand-mark"></span>
      <span class="cover__brand-name">Clearpath Living</span>
    </div>
    <div class="cover__photo" role="img" aria-label="One climber reaching down to help another up a rocky ridge"></div>
    <div class="url">www.clearpathliving.com</div>
  </article>
</section>

</body>
</html>
```